Business card design

I need my logo on this card, things I need the card to have on it
licensed and insured.
owner operators Milo & Dexter Hartwell
my phone number 5558203146
Disaster Recovery, Storm Damage Restoration, Proactive Disaster Plan Management, Roof Repair/Restoration Structural Repair and Reconstruction, Emergency Boarding and Tarping Service, Perimeter Fencing, Emergency Tree Removal,

```html
<!DOCTYPE html>
<html lang="en">
<head>
<meta charset="utf-8">
<title>Hartwell's Construction – Business Card</title>
<link rel="stylesheet" href="https://fonts.googleapis.com/css2?family=Montserrat:wght@400;500;600;700&display=swap">
<style>
  :root {
    --brand-blue: #1a87c2;
    --brand-grey: #737578;
    --ink: #3a3a3a;
    --card: #ffffff;
    --backdrop: #eceef0;
  }
  * { margin: 0; padding: 0; box-sizing: border-box; }
  html, body { width: 1200px; height: 1200px; overflow: hidden; }
  body {
    background: var(--backdrop);
    font-family: "Montserrat", Arial, sans-serif;
    position: relative;
  }
  .card {
    position: absolute;
    left: 225px;
    width: 812px;
    height: 465px;
    background: var(--card);
    overflow: hidden;
  }
  .card--front { top: 110px; }
  .card--back { top: 637px; }

  .company-name {
    position: absolute;
    color: var(--brand-blue);
    font-weight: 600;
    font-size: 30px;
    line-height: 1.15;
    letter-spacing: 0.5px;
  }
  .card--front .company-name {
    left: 52px;
    top: 60px;
    width: 320px;
  }
  .card--back .company-name {
    left: 0;
    right: 0;
    top: 62px;
    text-align: center;
    font-size: 40px;
  }

  .holder-name {
    position: absolute;
    right: 69px;
    top: 196px;
    font-size: 40px;
    font-weight: 700;
    color: var(--brand-blue);
    letter-spacing: -0.5px;
    white-space: nowrap;
  }
  .title-rule {
    position: absolute;
    left: 0;
    right: 0;
    top: 250px;
    display: flex;
    align-items: center;
    height: 36px;
  }
  .title-rule__line { height: 2px; }
  .title-rule__line--blue { flex: 1; background: var(--brand-blue); }
  .title-rule__line--grey { width: 60px; background: var(--brand-grey); }
  .holder-title {
    padding: 0 10px;
    font-size: 24px;
    font-weight: 500;
    color: var(--brand-grey);
    letter-spacing: 1px;
    white-space: nowrap;
  }

  .contact-list {
    position: absolute;
    left: 50px;
    top: 292px;
    list-style: none;
  }
  .contact-item {
    display: flex;
    align-items: center;
    height: 36px;
    font-size: 24px;
    color: var(--ink);
  }
  .contact-icon {
    width: 28px;
    height: 28px;
    margin-right: 14px;
    flex: none;
  }

  .credential {
    position: absolute;
    left: 0; right: 0;
    top: 118px;
    text-align: center;
    font-size: 17px;
    font-weight: 500;
    letter-spacing: 6px;
    text-transform: uppercase;
    color: var(--brand-grey);
  }
  .service-list {
    position: absolute;
    left: 60px;
    right: 60px;
    top: 170px;
    list-style: none;
    display: grid;
    grid-template-columns: 1fr 1fr;
    column-gap: 30px;
    row-gap: 8px;
  }
  .service-item {
    font-size: 16px;
    color: var(--ink);
    line-height: 1.3;
    padding-left: 18px;
    position: relative;
  }
  .service-item::before {
    content: "";
    position: absolute;
    left: 0;
    top: 7px;
    width: 8px;
    height: 8px;
    background: var(--brand-blue);
  }

  .website {
    position: absolute;
    left: 0; right: 0;
    top: 388px;
    text-align: center;
    font-size: 30px;
    color: var(--brand-blue);
    letter-spacing: 0.5px;
  }

  .footer-band {
    position: absolute;
    left: 0;
    bottom: 0;
    width: 812px;
    height: 18px;
  }
</style>
</head>
<body>

<section class="card card--front">
  <div class="company-name">Hartwell's Construction L.L.C</div>

  <div class="holder-name">Milo &amp; Dexter Hartwell</div>
  <div class="title-rule">
    <span class="title-rule__line title-rule__line--blue"></span>
    <span class="holder-title">OWNER OPERATORS</span>
    <span class="title-rule__line title-rule__line--grey"></span>
  </div>

  <ul class="contact-list">
    <li class="contact-item">
      <svg class="contact-icon" viewBox="0 0 24 24" fill="none" stroke="var(--brand-blue)" stroke-width="2" stroke-linecap="round" stroke-linejoin="round">
        <path d="M5 3h3l2 5-2.5 1.5a11 11 0 0 0 7 7L16 14l5 2v3a2 2 0 0 1-2 2A16 16 0 0 1 3 5a2 2 0 0 1 2-2z"/>
      </svg>
      555 820 3146
    </li>
    <li class="contact-item">
      <svg class="contact-icon" viewBox="0 0 24 24" fill="none" stroke="var(--brand-blue)" stroke-width="1.6" stroke-linejoin="round">
        <path d="M3 10l9-7 9 7v11H3z"/>
        <path d="M3 10l9 6 9-6"/>
        <circle cx="12" cy="9" r="2.6"/>
      </svg>
      yourmail@hartwellbuild.com
    </li>
    <li class="contact-item">
      <svg class="contact-icon" viewBox="0 0 24 24" fill="none" stroke="var(--brand-blue)" stroke-width="1.6">
        <circle cx="12" cy="12" r="9.5"/>
        <ellipse cx="12" cy="12" rx="4" ry="9.5"/>
        <path d="M2.5 12h19M4 7h16M4 17h16"/>
      </svg>
      www.yourwebsite.com
    </li>
    <li class="contact-item">
      <svg class="contact-icon" viewBox="0 0 24 24">
        <path d="M12 2a6.5 6.5 0 0 0-6.5 6.5C5.5 13 12 19 12 19s6.5-6 6.5-10.5A6.5 6.5 0 0 0 12 2z" fill="var(--brand-blue)"/>
        <circle cx="12" cy="8.5" r="2.4" fill="#fff"/>
        <ellipse cx="12" cy="20.5" rx="7" ry="2" fill="none" stroke="var(--brand-blue)" stroke-width="1.5"/>
      </svg>
      Your Location Here
    </li>
  </ul>

  <svg class="footer-band" viewBox="0 0 812 18" preserveAspectRatio="none">
    <polygon points="0,0 568,0 550,18 0,18" fill="var(--brand-blue)"/>
    <polygon points="578,0 812,0 812,18 560,18" fill="var(--brand-grey)"/>
  </svg>
</section>

<section class="card card--back">
  <div class="company-name">Hartwell's Construction L.L.C</div>
  <div class="credential">Licensed and Insured</div>

  <ul class="service-list">
    <li class="service-item">Disaster Recovery</li>
    <li class="service-item">Storm Damage Restoration</li>
    <li class="service-item">Proactive Disaster Plan Management</li>
    <li class="service-item">Roof Repair / Restoration</li>
    <li class="service-item">Structural Repair and Reconstruction</li>
    <li class="service-item">Emergency Boarding and Tarping</li>
    <li class="service-item">Perimeter Fencing</li>
    <li class="service-item">Emergency Tree Removal</li>
  </ul>

  <div class="website">www.website.com</div>

  <svg class="footer-band" viewBox="0 0 812 18" preserveAspectRatio="none">
    <polygon points="0,0 238,0 256,18 0,18" fill="var(--brand-blue)"/>
    <polygon points="246,0 812,0 812,18 264,18" fill="var(--brand-grey)"/>
  </svg>
</section>

</body>
</html>
```